KGDB Business Card

Looking for a business card design to incorporate our branding. We want to only use the colors listing in the Branding Package (attached).
Updates

Target Market(s)

People who need their phone or device fixed.

Industry/Entity Type

Electronics

Contact Information for Business Card

Please use:

Bright Circuit Mending Depot LLC
3478 S Ridge Trail 2210 E
Suite 417
San Antonio, TX 78341

Marcus Delwyn, Store Manager

(210) 555-0143

Requirements
Must have
• Must include the colors that are contained within the Branding Package PDF file.

```html
<!DOCTYPE html>
<html lang="en">
<head>
<meta charset="utf-8">
<title>KGDB Business Card</title>
<link rel="stylesheet" href="https://fonts.googleapis.com/css2?family=Source+Sans+3:wght@400;600;700&display=swap">
<style>
  :root {
    --stage: #000000;
    --card: #333437;
    --brand-orange: #f0561a;
    --text-light: #f2f2f2;
    --divider: #45464a;
  }
  * { margin: 0; padding: 0; box-sizing: border-box; }
  html, body {
    width: 1200px;
    height: 900px;
    overflow: hidden;
    background: var(--stage);
    font-family: "Source Sans 3", sans-serif;
  }
  .canvas { position: relative; width: 1200px; height: 900px; }
  .card {
    position: absolute;
    top: 271px;
    width: 457px;
    height: 281px;
    background: var(--card);
    border-radius: 14px;
  }
  .card-front { left: 137px; }
  .card-back { left: 626px; }

  .brand-mark {
    position: absolute;
    background: var(--brand-orange);
    border-radius: 8px;
  }
  .brand-name {
    position: absolute;
    color: var(--brand-orange);
    font-weight: 700;
    white-space: nowrap;
  }
  .card-front .brand-mark { left: 49px; top: 121px; width: 40px; height: 40px; }
  .card-front .brand-name { left: 98px; top: 122px; font-size: 28px; line-height: 38px; }

  .divider {
    position: absolute;
    left: 217px;
    top: 84px;
    width: 1px;
    height: 115px;
    background: var(--divider);
  }

  .contact { position: absolute; left: 252px; top: 68px; color: var(--text-light); }
  .person-name { color: var(--brand-orange); font-weight: 700; font-size: 18px; line-height: 22px; }
  .person-role { font-size: 13px; line-height: 18px; margin-top: 1px; }
  .phone { display: flex; align-items: center; gap: 6px; font-size: 13px; line-height: 18px; margin-top: 15px; }
  .phone svg { width: 9px; height: 9px; }
  .company { color: var(--brand-orange); font-weight: 600; font-size: 13px; line-height: 18px; margin-top: 18px; }
  .address { font-size: 13px; line-height: 19px; }

  .card-back .brand-mark { left: 64px; top: 104px; width: 68px; height: 68px; border-radius: 10px; }
  .card-back .brand-name { left: 146px; top: 122px; font-size: 22px; line-height: 32px; font-weight: 600; }
</style>
</head>
<body>
<main class="canvas">
  <section class="card card-front">
    <span class="brand-mark"></span>
    <span class="brand-name">KGDB</span>
    <span class="divider"></span>
    <div class="contact">
      <p class="person-name">Marcus Delwyn</p>
      <p class="person-role">Store Manager</p>
      <p class="phone">
        <svg viewBox="0 0 10 10" aria-hidden="true"><path d="M2 0.5 L3.6 2.6 L2.7 3.6 Q3.8 5.9 6.3 7.2 L7.3 6.3 L9.5 7.8 L8.6 9.4 Q4.6 9.3 1.6 5.6 Q0.3 3.6 0.5 1.4 Z" fill="#f0561a"/></svg>
        <span>(210) 555-0143</span>
      </p>
      <p class="company">Bright Circuit Mending Depot LLC</p>
      <p class="address">3478 S Ridge Trail 2210 E Suite</p>
      <p class="address">417 San Antonio, TX 78341</p>
    </div>
  </section>

  <section class="card card-back">
    <span class="brand-mark"></span>
    <span class="brand-name">Bright Circuit Mending Depot</span>
  </section>
</main>
</body>
</html>
```